Photography Studio Prep Guide Design Needed

I have a prep guide I send to all parents who book a session - It is outdated and ugly. I want a gorgeous, clean, modern upscale look for the brochure I send.

I already have the text and can provide photos for the final design. I want the cover to be clean and upscale and modern, with a happy feel.

Target Market(s)

My clients for an upscale Newborn Photography Studio

Requirements
Must have
• space for my photos, an upscale clean feel
Nice to have
• I love color, but don't want the brochure to look busy. I love cream, white, pale pink.

```html
<!DOCTYPE html>
<html lang="en">
<head>
<meta charset="utf-8">
<title>Newborn Session Prep Guide</title>
<link href="https://fonts.googleapis.com/css2?family=Playfair+Display:wght@700&family=Josefin+Sans:wght@400;600&family=Parisienne&display=swap" rel="stylesheet">
<style>
  :root {
    --paper: #ffffff;
    --page-edge: #d8d8d8;
    --gold: #efb947;
    --blush: #f0cfcc;
    --blush-box: #efd8d7;
    --ink-soft: #8e8e8e;
    --ink-script: #6f6a6a;
    --footer-ink: #7a7a7a;
    --sunny: #f6e07a;
    --teal: #2f8f97;
    --dusk-blue: #5f8a9a;
    --slate: #3f4a58;
    --cream: #efe8df;
    --skin: #e7cfc2;
  }
  * { margin: 0; padding: 0; box-sizing: border-box; }
  html, body { width: 1200px; height: 1000px; overflow: hidden; background: var(--paper); }
  .canvas { position: relative; width: 1200px; height: 1000px; font-family: "Josefin Sans", sans-serif; }

  .spread { position: absolute; border: 2px solid var(--page-edge); background: var(--paper); display: flex; }
  .spread--inside { left: 20px; top: 130px; width: 571px; height: 369px; }
  .spread--faq { left: 611px; top: 132px; width: 570px; height: 369px; }
  .page { position: relative; height: 100%; }
  .spread--inside .page--left { width: 284px; border-right: 2px solid var(--page-edge); }
  .spread--inside .page--right { flex: 1; }
  .spread--faq .page--left { width: 283px; border-right: 2px solid var(--page-edge); }
  .spread--faq .page--right { flex: 1; }

  .page-footer {
    position: absolute; left: 0; right: 0; bottom: 11px; text-align: center;
    font-size: 7.2px; letter-spacing: 1.6px; text-transform: uppercase; color: var(--footer-ink);
  }

  .topic { position: absolute; width: 242px; }
  .topic h3 {
    font-family: "Playfair Display", serif; font-weight: 700; color: var(--gold);
    font-size: 9.4px; line-height: 11px; margin-bottom: 2px;
  }
  .topic p {
    font-size: 5.5px; line-height: 7.3px; color: var(--ink-soft); text-transform: uppercase; letter-spacing: 0.25px;
  }

  .photo { position: absolute; }
  .photo--newborn-band {
    left: 0; right: 0; top: 244px; height: 92px;
    background: linear-gradient(100deg, var(--sunny) 0%, var(--sunny) 26%, var(--teal) 30%, var(--teal) 62%, var(--sunny) 66%, var(--sunny) 100%);
  }
  .collage { position: absolute; left: 46px; top: 76px; width: 193px; height: 213px; }
  .photo--moon-boat { left: 0; top: 0; width: 95px; height: 123px; background: linear-gradient(180deg, #7fa5b3 0%, var(--dusk-blue) 55%, var(--slate) 100%); }
  .photo--cuddle { left: 98px; top: 0; width: 95px; height: 62px; background: linear-gradient(135deg, var(--cream), var(--skin)); }
  .tagline-box {
    position: absolute; left: 98px; top: 64px; width: 95px; height: 59px; background: var(--blush-box);
    display: flex; align-items: center; justify-content: center; text-align: center;
    font-family: "Parisienne", cursive; font-size: 11px; line-height: 19px; color: var(--ink-script);
  }
  .photo--tiny-feet { left: 0; top: 126px; width: 193px; height: 87px; background: linear-gradient(180deg, #f3ede6 0%, var(--skin) 55%, #efe7de 100%); }

  .guide-title {
    position: absolute; left: 29px; top: 22px;
    font-family: "Playfair Display", serif; font-weight: 700; color: var(--blush); font-size: 21px; line-height: 26px;
  }
  .guide-subtitle {
    position: absolute; right: 34px; top: 48px; font-size: 8.2px; letter-spacing: 1.3px; text-transform: uppercase; color: #6e6e6e;
  }
  .faq-title {
    position: absolute; left: 29px; top: 252px;
    font-family: "Playfair Display", serif; font-weight: 700; color: var(--blush); font-size: 21px; line-height: 26px;
  }

  .cover {
    position: absolute; left: 451px; top: 554px; width: 285px; height: 368px;
    border: 2px solid var(--page-edge);
    background: linear-gradient(180deg, #8fb3bf 0%, var(--dusk-blue) 45%, #4b6f80 68%, var(--slate) 100%);
  }
</style>
</head>
<body>
<div class="canvas">

  <section class="spread spread--inside">
    <div class="page page--left">
      <div class="topic" style="left:29px; top:23px;">
        <h3>Studio</h3>
        <p>If you are nursing please avoid eating anything spicy. Lorem ipsum dolor sit amet, consectetur adipiscing elit. Curabitur accumsan finibus mauris, id faucibus diam sagittis sed. Lorem ipsum dolor sit</p>
      </div>
      <div class="topic" style="left:29px; top:67px;">
        <h3>Your Role</h3>
        <p>Feed the baby as much as possible in the 24 hours preceeding your session. Lorem ipsum dolor sit amet, consectetur adipiscing elit. Curabitur accumsan finibus mauris, id faucibus diam sagittis sed.</p>
      </div>
      <div class="topic" style="left:29px; top:109px;">
        <h3>Time</h3>
        <p>Interact with and keep baby awake for 2 hours. Lorem ipsum dolor sit amet, consectetur adipiscing elit. Curabitur accumsan finibus mauris, id faucibus diam sagittis sed. Lorem ipsum dolor sit</p>
      </div>
      <div class="topic" style="left:29px; top:153px;">
        <h3>Family Photos / Clothing</h3>
        <p>Please dress baby in a simple loose sleeper we can unsnap when you arrive. Lorem ipsum dolor sit amet, consectetur adipiscing elit. Curabitur accumsan finibus mauris, id faucibus diam sagittis sed.</p>
      </div>
      <div class="topic" style="left:29px; top:199px;">
        <h3>Sibling Photos</h3>
        <p>Please bring a pacifier, it can be very helpful during a session. Lorem ipsum dolor sit amet, consectetur adipiscing elit. Curabitur accumsan finibus mauris, id faucibus diam sagittis sed.</p>
      </div>
      <div class="photo photo--newborn-band" role="img" aria-label="Three newborn portraits arranged in diagonal strips on yellow and teal backdrops"></div>
      <div class="page-footer">Clara Whitfield Photography</div>
    </div>
    <div class="page page--right">
      <div class="collage">
        <div class="photo photo--moon-boat" role="img" aria-label="Newborn sleeping in a small blue boat under a painted moon and stars"></div>
        <div class="photo photo--cuddle" role="img" aria-label="Parent cuddling a sleeping newborn"></div>
        <div class="tagline-box">Capturing life's<br>sweetest moments</div>
        <div class="photo photo--tiny-feet" role="img" aria-label="Close-up of newborn feet on a cream knit blanket"></div>
      </div>
      <div class="page-footer">Clara Whitfield Photography</div>
    </div>
  </section>

  <section class="spread spread--faq">
    <div class="page page--left">
      <h1 class="guide-title">What I Need To Know</h1>
      <div class="guide-subtitle">Before Your Session</div>
      <div class="topic" style="left:29px; top:73px;">
        <h3>Your Baby's Information</h3>
        <p>If you are nursing please avoid eating anything spicy. Lorem ipsum dolor sit amet, consectetur adipiscing elit. Curabitur accumsan finibus mauris, id faucibus diam sagittis sed. Lorem ipsum dolor sit</p>
      </div>
      <div class="topic" style="left:29px; top:117px;">
        <h3>Your Favorite Colors</h3>
        <p>Feed the baby as much as possible in the 24 hours preceeding your session. Lorem ipsum dolor sit amet, consectetur adipiscing elit. Curabitur accumsan finibus mauris, id faucibus diam sagittis sed.</p>
      </div>
      <div class="topic" style="left:29px; top:159px;">
        <h3>Specific Shots</h3>
        <p>Interact with and keep baby awake for 2 hours. Lorem ipsum dolor sit amet, consectetur adipiscing elit. Curabitur accumsan finibus mauris, id faucibus diam sagittis sed. Lorem ipsum dolor sit</p>
      </div>
      <div class="topic" style="left:29px; top:203px;">
        <h3>Siblings</h3>
        <p>Please dress baby in a simple loose sleeper we can unsnap when you arrive. Lorem ipsum dolor sit amet, consectetur adipiscing elit. Curabitur accumsan finibus mauris, id faucibus diam sagittis sed.</p>
      </div>
      <h2 class="faq-title">FAQ's</h2>
      <div class="topic" style="left:29px; top:295px;">
        <h3>When Will I See My Photos?</h3>
        <p>If you are nursing please avoid eating anything spicy. Lorem ipsum dolor sit amet, consectetur adipiscing elit. Curabitur accumsan finibus mauris, id faucibus diam sagittis sed.</p>
      </div>
      <div class="page-footer">Clara Whitfield Photography</div>
    </div>
    <div class="page page--right">
      <div class="topic" style="left:28px; top:25px;">
        <h3>Can I Share My Gallery?</h3>
        <p>If you are nursing please avoid eating anything spicy. Lorem ipsum dolor sit amet, consectetur adipiscing elit. Curabitur accumsan finibus mauris, id faucibus diam sagittis sed. Lorem ipsum dolor sit</p>
      </div>
      <div class="topic" style="left:28px; top:69px;">
        <h3>How Can I Download My Photos?</h3>
        <p>Feed the baby as much as possible in the 24 hours preceeding your session. Lorem ipsum dolor sit amet, consectetur adipiscing elit. Curabitur accumsan finibus mauris, id faucibus diam sagittis sed.</p>
      </div>
      <div class="topic" style="left:28px; top:112px;">
        <h3>What If My Baby Won't Sleep?</h3>
        <p>Interact with and keep baby awake for 2 hours. Lorem ipsum dolor sit amet, consectetur adipiscing elit. Curabitur accumsan finibus mauris, id faucibus diam sagittis sed. Lorem ipsum dolor sit</p>
      </div>
      <div class="topic" style="left:28px; top:155px;">
        <h3>What Poses Will You Do?</h3>
        <p>Please dress baby in a simple loose sleeper we can unsnap when you arrive. Lorem ipsum dolor sit amet, consectetur adipiscing elit. Curabitur accumsan finibus mauris, id faucibus diam sagittis sed.</p>
      </div>
      <div class="topic" style="left:28px; top:201px;">
        <h3>Will My Baby Be Safe?</h3>
        <p>Please bring a pacifier, it can be very helpful during a session. Lorem ipsum dolor sit amet, consectetur adipiscing elit. Curabitur accumsan finibus mauris, id faucibus diam sagittis sed.</p>
      </div>
      <div class="topic" style="left:28px; top:246px;">
        <h3>My Baby Has Acne?</h3>
        <p>Please dress baby in a simple loose sleeper we can unsnap when you arrive. Lorem ipsum dolor sit amet, consectetur adipiscing elit. Curabitur accumsan finibus mauris, id faucibus diam sagittis sed.</p>
      </div>
      <div class="topic" style="left:28px; top:291px;">
        <h3>How Many Props Can I Choose?</h3>
        <p>Please bring a pacifier, it can be very helpful during a session. Lorem ipsum dolor sit amet, consectetur adipiscing elit. Curabitur accumsan finibus mauris, id faucibus diam sagittis sed.</p>
      </div>
      <div class="page-footer">Clara Whitfield Photography</div>
    </div>
  </section>

  <section class="cover" role="img" aria-label="Cover photo: newborn in a knit crown sleeping in a blue toy boat with a white sail, under a painted moon and stars"></section>

</div>
</body>
</html>
```